Design professional, clean and neat beauty clinic

design an instagram style flyer similar style but have my own branding. Like they have their own. Must look different but also similar/better in professionalism. source file also needed.

Font styles to use
Sans Serif

```html
<!DOCTYPE html>
<html lang="en">
<head>
<meta charset="utf-8">
<title>Lavelle Aesthetics – Social Flyers</title>
<link rel="stylesheet" href="https://fonts.googleapis.com/css2?family=Montserrat:wght@300;400;500;600;700&family=Nunito+Sans:wght@300;400&display=swap">
<style>
  :root {
    --navy: #2f3a55;
    --lavender: #8b88c2;
    --ink: #3b3b3f;
    --soft: #f6f2f4;
    --paper: #ffffff;
    --mist: #ececf1;
  }
  html, body { margin: 0; padding: 0; overflow: hidden; }
  body { width: 848px; height: 1200px; background: var(--paper); position: relative; font-family: "Nunito Sans", sans-serif; color: var(--ink); }

  .post { position: absolute; width: 359px; height: 359px; overflow: hidden; background: var(--paper); box-shadow: 0 2px 6px rgba(0,0,0,0.08); }
  .post > * { position: absolute; }
  .post--lift { left: 245px; top: 17px; background: linear-gradient(90deg, #f4f4f7, #e6e6ec); }
  .post--contour { left: 38px; top: 400px; }
  .post--courses { left: 464px; top: 400px; }
  .post--win { left: 38px; top: 787px; }
  .post--july { left: 464px; top: 787px; }

  .footer-bar { left: 0; bottom: 0; width: 100%; height: 24px; background: var(--navy); color: #fff; font-family: "Montserrat", sans-serif; font-weight: 500; font-size: 7.4px; letter-spacing: 1.1px; line-height: 24px; text-align: center; z-index: 3; }

  .brand { font-family: "Montserrat", sans-serif; font-weight: 300; color: var(--ink); text-align: center; line-height: 1.1; letter-spacing: 3px; text-transform: uppercase; }
  .brand .brand-name { display: block; font-size: 15px; }
  .brand .brand-sub { display: block; font-size: 7px; letter-spacing: 3px; margin-top: 4px; }

  .heading { font-family: "Montserrat", sans-serif; font-weight: 700; letter-spacing: 2px; color: var(--ink); margin: 0; line-height: 1; }
  .accent { color: var(--lavender); }
  .body-copy { font-family: "Nunito Sans", sans-serif; font-weight: 400; font-size: 10px; line-height: 13px; margin: 0; }
  .photo { display: block; }

  /* Lift & Restore */
  .post--lift .brand { left: 16px; top: 22px; }
  .post--lift .photo { left: 170px; top: 0; width: 189px; height: 335px; background: radial-gradient(ellipse at 60% 45%, #b98a6c 0%, #9b6b51 35%, rgba(200,170,150,0.3) 70%, rgba(230,230,236,0) 100%), linear-gradient(90deg, rgba(236,236,241,0), #3a2a24 95%); }
  .post--lift .title-1 { left: 18px; top: 82px; font-size: 27px; }
  .post--lift .title-2 { left: 18px; top: 116px; font-size: 27px; }
  .post--lift .title-3 { left: 18px; top: 151px; font-size: 16px; font-weight: 400; letter-spacing: 2px; color: var(--lavender); }
  .post--lift .copy-1 { left: 18px; top: 181px; width: 195px; }
  .post--lift .copy-2 { left: 18px; top: 247px; width: 190px; }
  .post--lift .price-row { left: 18px; top: 300px; display: flex; align-items: center; gap: 8px; font-size: 10px; letter-spacing: 1px; }
  .pill { background: var(--lavender); color: #fff; border-radius: 3px; padding: 1px 4px; font-family: "Montserrat", sans-serif; font-weight: 400; letter-spacing: 1px; }

  /* Contour */
  .post--contour .photo { left: 0; top: 0; width: 359px; height: 250px; background: linear-gradient(180deg, #b79e90 0%, #c7b0a3 35%, #ded1ca 65%, rgba(255,255,255,0) 100%); }
  .post--contour .title-1 { left: 0; width: 359px; top: 178px; font-size: 26px; text-align: center; }
  .post--contour .title-2 { left: 0; width: 359px; top: 209px; font-size: 26px; text-align: center; }
  .post--contour .copy { left: 75px; width: 210px; top: 247px; text-align: center; }
  .post--contour .package-tag { left: 119px; top: 298px; display: flex; height: 17px; font-family: "Montserrat", sans-serif; font-size: 10.5px; letter-spacing: 1.5px; color: #fff; line-height: 17px; }
  .package-tag .label { background: var(--lavender); width: 82px; text-align: center; font-weight: 300; }
  .package-tag .amount { background: var(--ink); width: 39px; text-align: center; }
  .post--contour .brand { left: 270px; top: 292px; width: 86px; }
  .post--contour .brand .brand-name { font-size: 11px; letter-spacing: 2px; }
  .post--contour .brand .brand-sub { font-size: 6px; letter-spacing: 2px; }

  /* Courses */
  .post--courses .brand { left: 14px; top: 52px; width: 125px; }
  .post--courses .circle-art { left: 0; top: 0; z-index: 2; }
  .post--courses .offer-band { left: 0; top: 138px; width: 160px; height: 23px; background: var(--navy); color: #fff; font-family: "Montserrat", sans-serif; font-weight: 700; font-size: 12px; letter-spacing: 1.5px; line-height: 23px; padding-left: 19px; box-sizing: border-box; z-index: 1; }
  .post--courses .title-1 { left: 9px; top: 179px; font-size: 21px; letter-spacing: 1.5px; }
  .post--courses .title-2 { left: 9px; top: 202px; font-size: 23px; letter-spacing: 1.5px; }
  .post--courses .course-strip { left: 0; top: 245px; width: 359px; height: 90px; background: var(--soft); display: flex; }
  .course { flex: 1; text-align: center; padding-top: 25px; font-size: 8.5px; line-height: 11px; position: relative; }
  .course .date { display: block; font-family: "Montserrat", sans-serif; color: var(--lavender); font-size: 9px; letter-spacing: 0.5px; }
  .course .price { position: absolute; left: 50%; top: 64px; transform: translateX(-50%); font-size: 10px; }
  .post--courses .divider { top: 264px; width: 1px; height: 53px; background: var(--lavender); }

  /* Win */
  .post--win .photo { left: 180px; top: 0; width: 179px; height: 335px; background: linear-gradient(160deg, #e5e3e4 0%, #d8c6bb 40%, #c79f88 65%, #e7e4ea 100%); }
  .post--win .brand { left: 0; width: 180px; top: 28px; }
  .post--win .win { left: 0; width: 180px; top: 92px; font-size: 33px; text-align: center; letter-spacing: 3px; color: var(--lavender); }
  .post--win .summer { left: 0; width: 180px; top: 131px; font-size: 14.5px; text-align: center; letter-spacing: 1.5px; }
  .post--win .bff { left: 0; width: 180px; top: 148px; font-family: "Montserrat", sans-serif; font-size: 9.5px; text-align: center; color: var(--lavender); letter-spacing: 1.5px; }
  .prize-pill { left: 27px; width: 124px; height: 14px; border-radius: 4px; background: var(--lavender); color: #fff; font-family: "Montserrat", sans-serif; font-weight: 600; font-size: 9px; letter-spacing: 2px; line-height: 14px; text-align: center; }
  .prize-copy { left: 0; width: 180px; text-align: center; font-size: 10px; line-height: 13px; }
  .post--win .terms { left: 7px; top: 321px; font-size: 9.5px; }

  /* July */
  .post--july .brand { left: 0; width: 359px; top: 18px; }
  .post--july .brand .brand-name { font-size: 13px; }
  .post--july .brand .brand-sub { font-size: 5.5px; }
  .post--july .title { left: 0; width: 359px; top: 60px; font-size: 20px; text-align: center; letter-spacing: 2.5px; }
  .tile { width: 170px; height: 110px; overflow: hidden; }
  .tile .photo { position: absolute; inset: 0; }
  .tile .caption { position: absolute; left: 0; bottom: 0; width: 100%; height: 45px; background: linear-gradient(90deg, rgba(47,58,85,0.92), rgba(47,58,85,0.55)); color: #fff; font-family: "Montserrat", sans-serif; font-size: 8px; letter-spacing: 0.3px; line-height: 11px; box-sizing: border-box; padding: 12px 48px 0 8px; white-space: nowrap; }
  .tile .pill { position: absolute; right: 6px; top: 13px; font-size: 10px; padding: 2px 5px; }
  .tile--a { left: 0; top: 90px; }
  .tile--b { left: 189px; top: 90px; }
  .tile--c { left: 0; top: 215px; }
  .tile--d { left: 189px; top: 215px; }
  .tile--a .photo { background: linear-gradient(180deg, #eae3dc, #d7c0ae 60%, #c8ad9a); }
  .tile--b .photo { background: linear-gradient(160deg, #f3f3f5, #dfd9d7 50%, #c9b6aa); }
  .tile--c .photo { background: linear-gradient(180deg, #f1ebe7, #e4cfc3 60%, #d2bdb1); }
  .tile--d .photo { background: linear-gradient(180deg, #c98f78, #d7a08f 50%, #e2c2b7); }
</style>
</head>
<body>

<section class="post post--lift">
  <div class="photo" role="img" aria-label="Photo of a smiling woman with curly hair touching her cheeks"></div>
  <div class="brand"><span class="brand-name">Lavelle</span><span class="brand-sub">Aesthetics</span></div>
  <h2 class="heading title-1">LIFT<span class="accent">&amp;</span></h2>
  <h2 class="heading title-2">RESTORE</h2>
  <div class="heading title-3">PACKAGE</div>
  <p class="body-copy copy-1">The lift and restore package consists of 4ml of premium product which can be used in the mid and lower face to restore volume loss.</p>
  <p class="body-copy copy-2">Restoring that volume loss will help to reverse the signs of ageing and leave you feeling and looking fresher.</p>
  <div class="price-row"><span class="pill">£475</span><span>Usually £575</span></div>
  <div class="footer-bar">CALL 0121 496 0732 OR BOOK ONLINE AT LV-AESTHETICS.CO.UK</div>
</section>

<section class="post post--contour">
  <div class="photo" role="img" aria-label="Photo of a woman receiving a forehead injection treatment"></div>
  <h2 class="heading title-1">6ML <span class="accent">CONTOUR</span></h2>
  <h2 class="heading title-2">&amp; <span class="accent">SCULPT</span></h2>
  <p class="body-copy copy">Providing noticeable results in reducing unwanted lines and wrinkles resulting in a smoother younger look.</p>
  <div class="package-tag"><span class="label">PACKAGE</span><span class="amount">£475</span></div>
  <div class="brand"><span class="brand-name">Lavelle</span><span class="brand-sub">Aesthetics</span></div>
  <div class="footer-bar">CALL 0121 496 0732 OR BOOK ONLINE AT LV-AESTHETICS.CO.UK</div>
</section>

<section class="post post--courses">
  <div class="brand"><span class="brand-name">Lavelle</span><span class="brand-sub">Aesthetics</span></div>
  <div class="offer-band">SPECIAL OFFER</div>
  <h2 class="heading title-1">UPCOMING</h2>
  <h2 class="heading title-2 accent">COURSES</h2>
  <div class="course-strip">
    <div class="course"><span class="date">6TH APRIL</span>LV Foundation Dermal<br>Filler Course<span class="pill price">£250</span></div>
    <div class="course"><span class="date">8TH APRIL</span>LV Lip Masterclass<span class="pill price">£600</span></div>
    <div class="course"><span class="date">11TH APRIL</span>LV Foundation Anti-<br>Wrinkle Course<span class="pill price">£250</span></div>
  </div>
  <div class="divider" style="left:130px"></div>
  <div class="divider" style="left:239px"></div>
  <svg class="circle-art" width="359" height="359" viewBox="0 0 359 359" role="img" aria-label="Circular photo of a woman receiving a cheek filler injection">
    <defs>
      <linearGradient id="courseShade" x1="0" y1="0" x2="1" y2="1">
        <stop offset="0" stop-color="#d9d6dc"/>
        <stop offset="0.5" stop-color="#6b4233"/>
        <stop offset="1" stop-color="#3e2820"/>
      </linearGradient>
    </defs>
    <circle cx="288" cy="120" r="138" fill="url(#courseShade)" stroke="#8b88c2" stroke-width="4"/>
  </svg>
  <div class="footer-bar">CALL 0121 496 0732 OR BOOK ONLINE AT LV-AESTHETICS.CO.UK</div>
</section>

<section class="post post--win">
  <div class="photo" role="img" aria-label="Photo of a woman receiving a lip filler treatment from a gloved practitioner"></div>
  <div class="brand"><span class="brand-name">Lavelle</span><span class="brand-sub">Aesthetics</span></div>
  <h2 class="heading win">WIN</h2>
  <div class="heading summer">THIS SUMMER</div>
  <div class="bff">FOR YOU + YOUR BFF</div>
  <div class="prize-pill" style="top:175px">FIRST PRIZE</div>
  <p class="body-copy prize-copy" style="top:197px">2 x Radiance Package<br>3ml filler + cheek sculpt<br>Valued at £300</p>
  <div class="prize-pill" style="top:249px">SECOND PRIZE</div>
  <p class="body-copy prize-copy" style="top:272px">2 x Radiance Package<br>3ml filler + cheek sculpt<br>Valued at £300</p>
  <div class="terms">*T&amp;C’s apply</div>
  <div class="footer-bar">CALL 0121 496 0732 OR BOOK ONLINE AT LV-AESTHETICS.CO.UK</div>
</section>

<section class="post post--july">
  <div class="brand"><span class="brand-name">Lavelle</span><span class="brand-sub">Aesthetics</span></div>
  <h2 class="heading title"><span class="accent">JULY</span> OFFERS</h2>
  <div class="tile tile--a">
    <div class="photo" role="img" aria-label="Photo of a forehead anti-wrinkle treatment"></div>
    <div class="caption">2ML ANTI-WRINKLE<br>+ 1ML FILLER<span class="pill">£475</span></div>
  </div>
  <div class="tile tile--b">
    <div class="photo" role="img" aria-label="Photo of a laser hair removal treatment"></div>
    <div class="caption">LASER HAIR REMOVAL<br>UNDERARMS + BRAZILIAN<span class="pill">£50</span></div>
  </div>
  <div class="tile tile--c">
    <div class="photo" role="img" aria-label="Photo of a derma rolling facial treatment"></div>
    <div class="caption">DERMA ROLLING<br>FACE + DECOLLETAGE<span class="pill">£120</span></div>
  </div>
  <div class="tile tile--d">
    <div class="photo" role="img" aria-label="Close-up photo of a lip enhancement injection"></div>
    <div class="caption">LIP ENHANCEMENT<br>3ML<span class="pill">£50</span></div>
  </div>
  <div class="footer-bar">CALL 0121 496 0732 OR BOOK ONLINE AT LV-AESTHETICS.CO.UK</div>
</section>

</body>
</html>
```